Newspaper ad for web design services

I have a paid space in a local newspaper size: 4.5085" W x 2.6875" H.
I want to use it for promoting my web design services.
Designers have the freedom to design the ad and the offer.
The goal is to have people contact me for business web design.
I published one ad last month and it totally failed to bring any attention.
Feel free to change or add anything you think can be more effective to attract potential customers (I can create any tripwire you consider will work)
Target: Houston-based business owners looking to get a new website or to update their existing one.

```html
<!DOCTYPE html>
<html lang="en">
<head>
<meta charset="utf-8">
<title>Norte Designs – Newspaper Ad</title>
<link rel="stylesheet" href="https://fonts.googleapis.com/css2?family=Lato:wght@400;700;900&family=Quicksand:wght@600;700&display=swap">
<style>
  :root {
    --stage: #262626;
    --white: #ffffff;
    --navy: #1b2a6b;
    --navy-deep: #17235a;
    --blue: #0a56ee;
    --blue-bright: #1d64f5;
    --violet: #7b54ef;
    --pink: #e86cf0;
    --pink-soft: #f19af5;
    --ink: #111111;
  }
  * { margin: 0; padding: 0; box-sizing: border-box; }
  html, body {
    width: 1200px; height: 1200px; overflow: hidden;
    background: var(--stage);
  }
  .ad {
    position: absolute; left: 66px; top: 266px;
    width: 1080px; height: 646px;
    background: var(--white); overflow: hidden;
    font-family: "Lato", sans-serif;
  }
  .ad-shapes { position: absolute; inset: 0; }
  .brand {
    position: absolute; left: 66px; top: 24px; height: 58px;
    display: flex; align-items: center; gap: 16px;
  }
  .brand-mark { width: 54px; height: 54px; border-radius: 10px; background: var(--blue); }
  .brand-name {
    font-family: "Quicksand", sans-serif; font-weight: 700;
    font-size: 56px; color: var(--ink); letter-spacing: -0.5px;
  }
  .offer {
    position: absolute; left: 748px; top: 52px; width: 330px;
    transform: rotate(5deg); transform-origin: center;
    text-align: center; color: var(--white); white-space: nowrap;
  }
  .offer-lead { font-size: 33px; font-weight: 400; line-height: 38px; }
  .offer-main { font-size: 44px; font-weight: 900; line-height: 48px; }
  .offer-main .free { color: var(--navy); }
  .headline {
    position: absolute; left: 64px; top: 136px;
    font-size: 44px; font-weight: 900; line-height: 48px;
    color: var(--white); text-transform: uppercase; white-space: nowrap;
  }
  .headline .accent { color: var(--pink); }
  .headline-glow {
    position: absolute; left: 56px; top: 286px; width: 200px; height: 4px;
    border-radius: 2px;
    background: linear-gradient(90deg, transparent, #9fd2ff 40%, #ffffff 60%, transparent);
    box-shadow: 0 0 10px #7fc0ff;
  }
  .benefits { position: absolute; left: 16px; top: 340px; list-style: none; }
  .benefit {
    position: absolute; width: 220px;
    font-size: 22px; font-weight: 700; line-height: 25px;
    color: var(--white); text-transform: uppercase;
    padding-left: 50px;
  }
  .benefit svg { position: absolute; left: 0; top: 2px; width: 40px; height: 42px; }
  .benefit.c2 { left: 216px; }
  .benefit.r2 { top: 84px; }
  .visit {
    position: absolute; left: 132px; top: 535px; width: 186px; height: 42px;
    background: var(--pink); border: 3px solid var(--white); border-radius: 8px;
    color: var(--white); font-size: 26px; font-weight: 700;
    letter-spacing: 8px; text-align: center; line-height: 36px;
    box-shadow: 0 2px 4px rgba(0,0,0,.25);
  }
  .site {
    position: absolute; left: 30px; top: 588px;
    display: flex; align-items: center; gap: 12px;
    font-size: 36px; font-weight: 700; color: var(--navy);
  }
  .site .domain { color: var(--blue); }
  .site svg { width: 30px; height: 30px; }
  .screen-art {
    position: absolute; left: 460px; top: 340px; width: 348px; height: 288px;
    border-radius: 6px;
    background: linear-gradient(180deg, #23262d 0%, #e6e9f8 8%, #d9ddf5 70%, #b9bcc4 100%);
  }
  .video-frame {
    position: absolute; left: 808px; top: 238px; width: 260px; height: 196px;
    background: var(--pink); transform: rotate(-3deg);
  }
  .video-still {
    position: absolute; left: 816px; top: 228px; width: 248px; height: 192px;
    transform: rotate(-3deg);
    background: linear-gradient(135deg, #3b3733 0%, #6a5a50 45%, #2b2a2a 100%);
  }
  .cursor { position: absolute; left: 978px; top: 418px; width: 44px; height: 60px; }
</style>
</head>
<body>
  <main class="ad">
    <svg class="ad-shapes" viewBox="0 0 1080 646" width="1080" height="646" aria-hidden="true">
      <defs>
        <linearGradient id="panel" x1="0" y1="0" x2="1" y2="0">
          <stop offset="0" stop-color="#1b2a6b"/>
          <stop offset="0.55" stop-color="#1d3a9c"/>
          <stop offset="1" stop-color="#0a56ee"/>
        </linearGradient>
      </defs>
      <rect x="0" y="100" width="1080" height="462" fill="var(--blue)"/>
      <polygon points="0,100 768,100 672,553 0,553" fill="url(#panel)"/>
      <polygon points="720,100 770,100 676,553 646,553" fill="var(--violet)" opacity="0.85"/>
      <rect x="0" y="553" width="1080" height="9" fill="var(--pink)"/>
      <polygon points="708,50 1080,58 1080,182 780,160" fill="var(--navy-deep)"/>
      <polygon points="720,24 1080,24 1080,168 774,142" fill="var(--pink)"/>
      <polygon points="770,616 1044,616 1056,632 778,632" fill="var(--navy-deep)"/>
      <polygon points="822,493 960,493 1036,616 762,616" fill="var(--pink)"/>
      <rect x="904" y="512" width="72" height="70" rx="14" fill="var(--pink-soft)" opacity="0.6"/>
    </svg>

    <div class="brand">
      <span class="brand-mark"></span>
      <span class="brand-name">Norte Designs</span>
    </div>

    <div class="offer">
      <div class="offer-lead">Download Our</div>
      <div class="offer-main"><span class="free">FREE</span> E-BOOK</div>
    </div>

    <h1 class="headline">Make your<br>business website<br><span class="accent">double your sales!</span></h1>
    <div class="headline-glow"></div>

    <ul class="benefits">
      <li class="benefit"><svg viewBox="0 0 40 42"><rect x="2" y="8" width="30" height="30" fill="none" stroke="var(--pink)" stroke-width="4"/><path d="M9 22 L17 31 L37 4" fill="none" stroke="var(--pink)" stroke-width="5" stroke-linecap="round"/></svg>Get more customers</li>
      <li class="benefit c2"><svg viewBox="0 0 40 42"><rect x="2" y="8" width="30" height="30" fill="none" stroke="var(--pink)" stroke-width="4"/><path d="M9 22 L17 31 L37 4" fill="none" stroke="var(--pink)" stroke-width="5" stroke-linecap="round"/></svg>Increase sales</li>
      <li class="benefit r2"><svg viewBox="0 0 40 42"><rect x="2" y="8" width="30" height="30" fill="none" stroke="var(--pink)" stroke-width="4"/><path d="M9 22 L17 31 L37 4" fill="none" stroke="var(--pink)" stroke-width="5" stroke-linecap="round"/></svg>Get more reviews</li>
      <li class="benefit c2 r2"><svg viewBox="0 0 40 42"><rect x="2" y="8" width="30" height="30" fill="none" stroke="var(--pink)" stroke-width="4"/><path d="M9 22 L17 31 L37 4" fill="none" stroke="var(--pink)" stroke-width="5" stroke-linecap="round"/></svg>Refer more customers</li>
    </ul>

    <div class="visit">VISIT</div>

    <div class="site">
      <svg viewBox="0 0 30 30" aria-hidden="true"><g fill="none" stroke="var(--navy)" stroke-width="2.4"><circle cx="15" cy="15" r="12"/><ellipse cx="15" cy="15" rx="5.5" ry="12"/><line x1="3" y1="15" x2="27" y2="15"/></g></svg>
      <span>norte-<span class="domain">designs.com</span></span>
    </div>

    <div class="screen-art" role="img" aria-label="Illustration of a desktop monitor showing a website layout"></div>

    <div class="video-frame"></div>
    <div class="video-still" role="img" aria-label="Video still of the designer recording at a microphone, holding a mug"></div>

    <svg class="cursor" viewBox="0 0 44 60" aria-hidden="true">
      <path d="M4 4 L4 46 L15 36 L23 56 L31 52 L23 33 L38 33 Z" fill="var(--white)" stroke="var(--navy)" stroke-width="2"/>
    </svg>
  </main>
</body>
</html>
```